The Hollow - Short Film Poster Design

A short film that follows a forest ranger contemplating suicide as he stumbles upon three kids lost in the forest, each in their own, different way.

Genre: Contemporary Dark Drama

Seeking a poster that really stands out as a 'Festival Piece'. See the following lists for references:

QRVN Festival Poster Awards: https://www.snapvault.example/photos/officialqrvn/with/48203917562/

Here is the FULL RESOLUTION short film to take screen grabs and reference photos from:
https://www.filecrate.example/s/kp7wq2rzt91mxe4/Hollow014.mov?oref=e

We are open to much of anything, but this project needs to stand out as unique. On top of that, we are trying to push the angle of strangers LOST in the forest (hence the name) and have thought of the opening sequence of the young man walking through the woods on the epic wide shot of being used for the poster art.

Various items need to be included on the poster: (Please feel free to reword as appropriate)

1) A FILM BY GORDON FAIRWEATHER
2) A DENNIS HOLMGRAVE PRODUCTION

All other taglines are optional and subject to addition or removal.

Please message with all other questions and comments.
Updates

Hey everyone, I apologize for not providing a high enough resolution copy of the short. I was told that this was the highest resolution until I got back straight from my editor who said it's a preliminary. Unfortunately, I do not have the ENTIRE film at top resolution. I will, however, attach high resolution .tiffs from various points of the film for use. https://www.filecrate.example/sh/wte8pqz41nd75ub/BBXKTmcPoLRWqDYe27fhZwNtb?dl=0

Industry/Entity Type

Film Production

Font styles to use
Serif
Sans Serif

Requirements
Must have
• 1) A FILM BY GORDON FAIRWEATHER
• 2) A DENNIS HOLMGRAVE PRODUCTION
• "THE HOLLOW" - Name of Film
Nice to have
• Tagline, but not necessary.

```html
<!DOCTYPE html>
<html lang="en">
<head>
<meta charset="utf-8">
<title>The Hollow — Poster</title>
<link rel="stylesheet" href="https://fonts.googleapis.com/css2?family=Cinzel:wght@400;600;700&family=Cormorant+SC:wght@500;600&display=swap">
<style>
  :root {
    --forest-deep: #3a2f22;
    --forest-mid: #6b5a42;
    --forest-sage: #8e8a5c;
    --sky-pale: #e9e6dc;
    --signal-yellow: #f2dc14;
    --title-silver: #e6e2e8;
    --credit-white: #ffffff;
  }
  html, body {
    margin: 0;
    padding: 0;
    width: 810px;
    height: 1200px;
    overflow: hidden;
    background: var(--forest-deep);
  }
  .poster {
    position: relative;
    width: 810px;
    height: 1200px;
    overflow: hidden;
    font-family: "Cinzel", "Trajan Pro", serif;
  }
  .poster__scene {
    position: absolute;
    inset: 0;
    background:
      radial-gradient(ellipse at 92% 3%, var(--sky-pale) 0%, rgba(233,230,220,0) 18%),
      radial-gradient(ellipse at 45% 25%, rgba(160,150,90,0.55) 0%, rgba(160,150,90,0) 45%),
      linear-gradient(180deg, var(--forest-mid) 0%, var(--forest-sage) 30%, #5e5236 60%, var(--forest-deep) 100%);
  }
  .poster__glyph {
    position: absolute;
    color: var(--signal-yellow);
    opacity: 0.55;
    font-weight: 400;
    line-height: 1;
    font-style: italic;
    font-family: "Cormorant SC", "Cinzel", serif;
    pointer-events: none;
  }
  .poster__glyph--top {
    top: -150px;
    left: 230px;
    font-size: 620px;
    letter-spacing: -40px;
  }
  .poster__glyph--bottom {
    top: 1010px;
    left: 120px;
    font-size: 560px;
  }
  .poster__glyph--edge {
    top: 700px;
    left: -120px;
    font-size: 420px;
  }
  .poster__ghost {
    position: absolute;
    white-space: nowrap;
    color: rgba(40, 32, 20, 0.35);
    font-weight: 400;
    line-height: 1;
    pointer-events: none;
  }
  .poster__ghost--mid { top: 418px; left: 395px; font-size: 62px; }
  .poster__ghost--low { top: 955px; left: 105px; font-size: 72px; }
  .poster__ghost--base { top: 1048px; left: -30px; font-size: 118px; }
  .title-block {
    position: absolute;
    left: 84px;
    top: 502px;
  }
  .title-block__genre {
    margin: 0 0 6px 24px;
    font-family: "Cormorant SC", "Cinzel", serif;
    font-weight: 600;
    font-size: 16px;
    letter-spacing: 0.5px;
    color: var(--credit-white);
  }
  .title-block__title {
    margin: 0;
    font-weight: 700;
    line-height: 0.92;
  }
  .title-block__the {
    display: block;
    margin-left: 22px;
    font-size: 124px;
    color: var(--title-silver);
    text-shadow: 2px 3px 4px rgba(0,0,0,0.45);
  }
  .title-block__name {
    display: block;
    font-size: 118px;
    letter-spacing: -2px;
    color: var(--signal-yellow);
    text-shadow: 2px 3px 5px rgba(0,0,0,0.5);
  }
  .credits {
    position: absolute;
    left: 82px;
    top: 812px;
    color: var(--credit-white);
    font-weight: 600;
  }
  .credits p { margin: 0; }
  .credits__label { font-size: 27px; letter-spacing: 0.5px; }
  .credits__director { font-size: 29px; font-weight: 700; margin-top: 2px !important; }
  .credits__production { font-size: 26px; line-height: 1.18; margin-top: 22px !important; }
</style>
</head>
<body>
  <main class="poster">
    <div class="poster__scene" role="img" aria-label="Wide photograph of a young hiker with a red backpack walking through a dry, bare-branched forest valley"></div>

    <span class="poster__glyph poster__glyph--top" aria-hidden="true">HO</span>
    <span class="poster__glyph poster__glyph--edge" aria-hidden="true">/</span>
    <span class="poster__glyph poster__glyph--bottom" aria-hidden="true">O</span>

    <span class="poster__ghost poster__ghost--mid" aria-hidden="true">THE HOLLOW</span>
    <span class="poster__ghost poster__ghost--low" aria-hidden="true">THE HOLLOW</span>
    <span class="poster__ghost poster__ghost--base" aria-hidden="true">THE HOLLOW</span>

    <header class="title-block">
      <p class="title-block__genre">Contemporary Dark Drama</p>
      <h1 class="title-block__title">
        <span class="title-block__the">THE</span>
        <span class="title-block__name">HOLLOW</span>
      </h1>
    </header>

    <section class="credits">
      <p class="credits__label">A FILM BY</p>
      <p class="credits__director">GORDON FAIRWEATHER</p>
      <p class="credits__production">A DENNIS HOLMGRAVE<br>PRODUCTION</p>
    </section>
  </main>
</body>
</html>
```